Business Card Design

Copperfield Lantern & Spark, Inc. (CLS), located in Memphis, TN began operating on 2003. We are a certified
minority woman-owned business that genuinely takes a vested interest in our customers. We serve utilities,
government, contractors and end user markets in electrical, water, gas and industrial supplies. Our core
competency as a distributor of electrical materials has positioned us to serve business of all size. As your supply
chain partner, we arm you with the resources you need to make your supply chain more efficient. Our team
works with your team on a daily basis to help you solve problems and achieve goals. This team approach has
helped CLS customers to succeed and we can do the same for you.

NAICS Codes:
423610 Electrical Apparatus and Equipment, Wiring Supplies, and Related Equipment Merchant
Wholesalers
423510 Metal Service Centers and Other Metal Merchant Wholesalers
423720 Plumbing and Heating Equipment and Supplies (Hydronics) Merchant Wholesalers

Certifications
MBE (KRVPQAL, State of Tennessee Up-MRX and FJW), WBE (HQOLT),
WOSB, DOT (TDOT, MDOT, ALDOT, SCDOT, NCDOT, and VDOT), LOSB,
SBE, and LSB Certified
Some of Our Products Include:
. Boxes & Covers
. Conduit & Raceway
. Fittings
. Fuses
. Lamp & Ballasts
. Lighting Controls & Timers
. Lighting Fixtures
. Personal Safety
. Pipes
. Power Distribution
. Terminations Ground & Splices
. Tools & Testers
. Wire, Cords & Cable
. Wiring Devices
. Valves

Industry/Entity Type

Business

Contact Information for Business Card

Marianne T. Holloway - President/CEO
4728 Quillon Ave., Memphis, TN 38127
901-555-0147 office, 901-555-0182 fax, 901-555-0163 cell
mtholloway@clsllc-example.com - www.clsincorp-example.com

```html
<!DOCTYPE html>
<html lang="en">
<head>
<meta charset="utf-8">
<title>Copperfield Lantern &amp; Spark, Inc. – Business Card</title>
<link href="https://fonts.googleapis.com/css2?family=Open+Sans:wght@400;600&display=swap" rel="stylesheet">
<style>
  :root {
    --page: #e9e7e2;
    --card: #fbfbfa;
    --ink: #1d1d1b;
    --olive: #7d8c46;
    --olive-dark: #66733a;
    --muted: #b9bcb5;
  }
  * { box-sizing: border-box; margin: 0; padding: 0; }
  html, body { width: 1200px; height: 780px; overflow: hidden; }
  body {
    background: var(--page);
    font-family: "Open Sans", Arial, sans-serif;
    color: var(--ink);
    display: flex;
    align-items: center;
    justify-content: center;
    gap: 40px;
  }
  .card {
    position: relative;
    width: 560px;
    height: 320px;
    background: linear-gradient(135deg, #ffffff 0%, var(--card) 60%, #efefec 100%);
    box-shadow: 0 6px 18px rgba(0,0,0,.18);
    overflow: hidden;
  }
  .band {
    position: absolute;
    left: 0; right: 0; bottom: 0;
    height: 34px;
    background: var(--olive);
  }
  .wordmark {
    display: flex;
    align-items: center;
    gap: 10px;
    font-weight: 600;
    text-transform: uppercase;
    line-height: 1.1;
    letter-spacing: .5px;
    color: var(--ink);
  }
  .wordmark .mark {
    width: 14px; height: 14px;
    background: var(--olive);
    flex: none;
  }

  /* front */
  .card--front .social {
    position: absolute; top: 22px; right: 26px;
    display: flex; gap: 6px;
  }
  .card--front .social span {
    width: 20px; height: 20px; background: var(--muted); border-radius: 2px;
  }
  .card--front .wordmark {
    position: absolute; left: 32px; top: 58px;
    font-size: 22px; width: 250px;
  }
  .person {
    position: absolute; right: 30px; top: 88px; text-align: right;
  }
  .person .name { font-size: 21px; line-height: 28px; }
  .person .role { font-size: 15px; line-height: 20px; color: var(--olive); margin-top: 2px; }
  .rule {
    position: absolute; left: 32px; right: 30px; top: 150px;
    height: 1px; background: var(--olive);
  }
  .contacts {
    position: absolute; left: 32px; top: 168px;
    list-style: none; font-size: 14.5px; line-height: 22px;
  }
  .contacts li { display: flex; align-items: center; gap: 10px; }
  .contacts svg { width: 16px; height: 16px; flex: none; }
  .address {
    position: absolute; right: 30px; top: 180px;
    text-align: right; font-size: 15px; line-height: 22px;
  }

  /* back */
  .card--back .wordmark {
    position: absolute; left: 50%; top: 34px; transform: translateX(-50%);
    font-size: 25px; white-space: nowrap;
  }
  .tagline {
    position: absolute; left: 0; right: 0; top: 100px;
    text-align: center; font-size: 19px; color: var(--olive);
  }
  .products {
    position: absolute; left: 28px; right: 28px; top: 142px;
    font-size: 13.5px; line-height: 21px; text-align: center;
  }
  .card--back .band { display: flex; align-items: center; justify-content: center; }
  .url { color: #fff; font-size: 14px; letter-spacing: .3px; }
  .stripe {
    position: absolute; left: 0; right: 0; bottom: 40px; height: 3px; background: var(--olive-dark);
  }
</style>
</head>
<body>
  <section class="card card--front" aria-label="Card front">
    <div class="social" aria-hidden="true"><span></span><span></span><span></span><span></span></div>
    <div class="wordmark"><span class="mark"></span><span>Copperfield Lantern<br>&amp; Spark</span></div>
    <div class="person">
      <p class="name">Marianne T. Holloway</p>
      <p class="role">President/CEO</p>
    </div>
    <div class="rule"></div>
    <ul class="contacts">
      <li><svg viewBox="0 0 16 16"><rect width="16" height="16" fill="#7d8c46"/><path d="M5 4h2l1 2-1 1a5 5 0 0 0 2 2l1-1 2 1v2a1 1 0 0 1-1 1A7 7 0 0 1 4 5a1 1 0 0 1 1-1z" fill="#fff"/></svg>901-555-0147</li>
      <li><svg viewBox="0 0 16 16"><rect width="16" height="16" fill="#7d8c46"/><rect x="5" y="3" width="6" height="10" rx="1" fill="#fff"/></svg>901-555-0163</li>
      <li><svg viewBox="0 0 16 16"><rect width="16" height="16" fill="#7d8c46"/><rect x="3" y="6" width="10" height="6" fill="#fff"/><rect x="5" y="3" width="6" height="3" fill="#fff"/></svg>901-555-0182</li>
      <li><svg viewBox="0 0 16 16"><rect width="16" height="16" fill="#7d8c46"/><rect x="3" y="4" width="10" height="8" fill="#fff"/><path d="M3 4l5 4 5-4" stroke="#7d8c46" fill="none"/></svg>mtholloway@clsllc-example.com</li>
    </ul>
    <p class="address">4728 Quillon Ave<br>Memphis, TN 38127</p>
    <div class="band"></div>
  </section>

  <section class="card card--back" aria-label="Card back">
    <div class="wordmark"><span class="mark"></span><span>Copperfield Lantern &amp; Spark</span></div>
    <p class="tagline">Our Products Include</p>
    <p class="products">
      Boxes &amp; Covers | Conduit &amp; Raceway | Fittings | Fuses | Lamp &amp; Ballasts<br>
      Lighting Controls &amp; Timers | Lighting Fixtures | Personal Safety | Pipes<br>
      Power Distribution | Terminations Ground &amp; Splices | Tools &amp; Testers<br>
      Wire Cords &amp; Cable | Wiring Devices | Valves
    </p>
    <div class="stripe"></div>
    <div class="band"><span class="url">www.clsincorp-example.com</span></div>
  </section>
</body>
</html>
```